Fast Money - Simple Book Cover Design

Hello,

I am in need of a cover for my new book. The Book Title Is

"Standing Builder - Methods for Top Rated Web Feedback That Keeps Your Calendar Full and Draws Fresh Clients Through Your Gates!"

Author: Fireman Dale Prentiss

What I want: This is a book for businesses on improving their online reputation. I want to have 5 Stars on the cover. You can look at this quarvelfind search for ideas of what I am meaning.....

(copy and paste)

http://www.quarvelfind.example/lookup?q=5+star+online+reviews&mode=pics&page=1 (copy and paste)

I am open to different color schemes for the book. I am partial to dark blues if you make it look good. Here is another book that I really like the cover of....

http://www.brindlemart.example/Clipcast-Tactics-Growing-Outreach-ebook/item/ZX93KQ7TWP

I want the cover BOLD and to STAND OUT.

I am looking for a design to help establish me as an authority for online reputation marketing. This book will be both in Pagewell format and be used in print as well.

I am open to questions....

Thanks!

Dale

Reason: I don't believe we have received the right designs. I am going to give everyone more time...

Reason: Hi everyone, I had some stuff come up and was not able to be involved in this project. I am extending because we have not seen the exact thing we want and need time to work with designers to get it right. Thanks Dale

Reason: I am currently traveling and can't wrap this up until I get back.

Target Market(s)

Business Owners

Industry/Entity Type

Business

Requirements
Must have
• Title and Subtitle

Author Name

5 Stars Images....
Nice to have
• Creativity

Bold and stand out

Professional

Should not have
• thin text, small to read text, lame graphics,

```html
<!DOCTYPE html>
<html lang="en">
<head>
<meta charset="utf-8">
<title>Standing Builder – Book Cover</title>
<link rel="stylesheet" href="https://fonts.googleapis.com/css2?family=Ultra&family=Arimo:wght@700&display=swap">
<style>
  :root {
    --green-deep: #0f5a2a;
    --green-mid: #1e7a33;
    --green-glow: #3aa33a;
    --band-green: #6aaa2a;
    --frame-line: rgba(190, 230, 170, 0.55);
    --ink-white: #ffffff;
    --ink-black: #0b0b0b;
    --shadow: rgba(0, 0, 0, 0.55);
  }
  html, body {
    margin: 0;
    padding: 0;
    overflow: hidden;
    background: #ffffff;
  }
  .cover {
    position: relative;
    width: 900px;
    height: 1200px;
    overflow: hidden;
    background: radial-gradient(ellipse 62% 52% at 50% 40%, var(--green-glow) 0%, var(--green-mid) 45%, var(--green-deep) 100%);
  }
  .cover__frame {
    position: absolute;
    left: 27px;
    top: 27px;
    right: 27px;
    bottom: 27px;
    border: 2px solid var(--frame-line);
    pointer-events: none;
    z-index: 3;
  }
  .cover__title {
    position: absolute;
    left: 0;
    top: 0;
    width: 900px;
    height: 290px;
  }
  .cover__title text {
    font-family: "Ultra", serif;
    fill: var(--ink-white);
    font-size: 138px;
  }
  .cover__subtitle {
    position: absolute;
    right: 165px;
    top: 312px;
    margin: 0;
    font-family: "Arimo", sans-serif;
    font-weight: 700;
    font-size: 44px;
    line-height: 65px;
    color: var(--ink-white);
    text-align: right;
    text-shadow: 2px 3px 4px var(--shadow);
  }
  .cover__subtitle span { display: block; }
  .cover__stars {
    position: absolute;
    left: 0;
    top: 770px;
    width: 900px;
    height: 170px;
  }
  .cover__band {
    position: absolute;
    left: 0;
    right: 0;
    bottom: 0;
    height: 162px;
    background: var(--band-green);
    border-top: 2px solid rgba(255, 255, 255, 0.25);
  }
  .cover__author {
    position: absolute;
    left: 0;
    right: 0;
    top: 1078px;
    margin: 0;
    text-align: center;
    font-family: "Arimo", sans-serif;
    font-weight: 700;
    font-size: 48px;
    color: var(--ink-black);
    z-index: 4;
  }
</style>
</head>
<body>
  <main class="cover">
    <svg class="cover__title" viewBox="0 0 900 290" aria-label="Standing Builder">
      <text x="450" y="138" text-anchor="middle" textLength="720" lengthAdjust="spacingAndGlyphs">Standing</text>
      <text x="450" y="250" text-anchor="middle" textLength="620" lengthAdjust="spacingAndGlyphs">Builder</text>
    </svg>

    <h2 class="cover__subtitle">
      <span>Methods for Top Rated Web</span>
      <span>Feedback That Keeps Your</span>
      <span>Calendar Full and Draws</span>
      <span>Fresh Clients Through</span>
      <span>Your Gates!</span>
    </h2>

    <svg class="cover__stars" viewBox="0 0 900 170" aria-label="Five stars">
      <defs>
        <radialGradient id="star-gold" cx="50%" cy="50%" r="55%">
          <stop offset="0%" stop-color="#fff6b0"/>
          <stop offset="45%" stop-color="#f7d24a"/>
          <stop offset="100%" stop-color="#dc9a12"/>
        </radialGradient>
        <polygon id="star-shape" points="0,-78 18.3,-25.2 74.2,-24.1 29.7,9.6 45.8,63.1 0,31.2 -45.8,63.1 -29.7,9.6 -74.2,-24.1 -18.3,-25.2"/>
      </defs>
      <g fill="url(#star-gold)" stroke="#b37a10" stroke-width="2" stroke-linejoin="round">
        <use href="#star-shape" x="132" y="88"/>
        <use href="#star-shape" x="291" y="88"/>
        <use href="#star-shape" x="450" y="88"/>
        <use href="#star-shape" x="609" y="88"/>
        <use href="#star-shape" x="768" y="88"/>
      </g>
    </svg>

    <div class="cover__band"></div>
    <p class="cover__author">Fireman Dale Prentiss</p>
    <div class="cover__frame"></div>
  </main>
</body>
</html>
```